Personal Trainer website design

We are working with a personal trainer to design a website. They offer their primary services: Diet Coaching, In-Person Coaching (workouts), and Remote Coaching.
Some sites we like: https://www.mirabelfenn.com, https://kitarowe.com/en-us, https://bendwellstudio.co.uk
Thank you for taking the time to consider designing a website for us. We are web developers based in Stockton, CA USA. Most of our projects go through the same process. Understanding this process may help you win a project with us. We custom-code all of our websites in-house. We don’t have any requirements as to what tools you use for your design, but ask that you follow these guidelines.
IMAGES:
We ask that if you use any images, or icons in the design, have a link to the asset, so we can purchase the image/icon. Most of the designs we submit do not have the customer’s images on them unless they have some great images. Be creative; show us the feeling that you are trying to portray with your image choices. Use any royalty-free site you choose. We subscribe to Quillon and mostly use their images, but are ok to purchase images outside of Quillon.
FONTS:
We ask that you identify the fonts you’re using in the design. This can be done in a message if you want. We typically use Tembrik Fonts and Quillon Fonts.
CONTENT:
We're always open to different content and ideas. Often, we submit designs with stock images so that the client can see our vision. We typically go back and take pictures after the website launch to use their images with our vision. Lorem Ipsum is fine for paragraphs, but we ask that you make the Headers with correct English. We want to be able to show the vision and identify the sections of the website.
INSPIRATION:
We try and add a couple of links in the brief of some websites that we like to help you get started in your design.
REVISIONS:
We do not often ask for revisions of the designs unless we see something in the design that may not appeal to the client. If there are slight changes that we want to make, we simply do that in the development process.
FEEDBACK:
We rarely give feedback on designs during the design process. We are working on many website projects and do not have the time to give feedback. We usually respond if your request is well thought out and asks specific questions, but a note asking “feedback, please” usually goes unanswered.

```html
<!DOCTYPE html>
<html lang="en">
<head>
<meta charset="utf-8">
<title>Orbitfit – Personal Training</title>
<link rel="stylesheet" href="https://fonts.googleapis.com/css2?family=Poppins:wght@600;700;800&family=Outfit:wght@300;400;500&family=Oswald:wght@500;600&display=swap">
<style>
:root{
  --olive:#9aa51c;
  --olive-dark:#7e8806;
  --olive-light:#a8b22e;
  --ink:#333333;
  --ink-soft:#555555;
  --navy:#2d3a55;
  --white:#ffffff;
  --footer:#2b2b2b;
}
*{margin:0;padding:0;box-sizing:border-box}
html,body{width:1200px;height:3989px;overflow:hidden}
body{position:relative;background:var(--white);font-family:"Outfit",sans-serif;color:var(--ink)}
.abs{position:absolute}
/* hero */
.hero{left:0;top:0;width:1200px;height:830px}
.brand{left:165px;top:62px;display:flex;align-items:center;gap:14px;font-family:"Poppins",sans-serif;font-weight:700;font-size:50px;letter-spacing:2px;color:var(--ink)}
.brand-dot{width:30px;height:30px;border-radius:50%;background:var(--olive)}
.nav{left:577px;top:84px;display:flex;gap:45px;font-family:"Oswald",sans-serif;font-weight:500;font-size:14px;color:var(--ink)}
.hero-title{left:572px;top:152px;font-family:"Poppins",sans-serif;font-weight:700;color:var(--ink);line-height:1}
.hero-title .l1,.hero-title .l3{display:block;font-size:25px}
.hero-title .l2{display:block;font-size:36px;color:var(--olive);margin:12px 0 14px}
/* intro */
.eyebrow{font-size:17px;color:var(--olive-dark)}
.intro{left:163px;top:952px;width:420px}
.intro h1{font-family:"Poppins",sans-serif;font-weight:700;font-size:48px;line-height:48px;margin-top:20px;color:var(--ink)}
.rule{width:40px;height:2px;background:var(--olive-dark)}
.intro .rule{margin:40px 0 30px}
.intro p{font-size:15px;line-height:25px;color:var(--navy)}
.card{width:190px;height:207px;border-radius:10px;background:linear-gradient(160deg,var(--olive-dark),var(--olive-light));color:var(--white);padding:24px 23px}
.card .ico{width:48px;height:48px;border-radius:50%;background:var(--white);display:flex;align-items:center;justify-content:center}
.card h3{font-family:"Outfit",sans-serif;font-weight:400;font-size:20px;margin:18px 0 10px}
.card p{font-size:12px;line-height:19px}
/* testimonials */
.reviews-bg{left:0;top:1450px;width:1200px;height:870px}
.reviews-title{left:0;top:1682px;width:1200px;text-align:center;font-family:"Poppins",sans-serif;font-weight:800;font-size:50px;line-height:49px;color:var(--white)}
.quote{width:269px;height:231px;background:var(--white);border-radius:8px;padding:30px 23px}
.quote p{font-size:14px;line-height:25px;color:var(--navy)}
.person{display:flex;align-items:center;gap:12px;margin-top:12px}
.avatar{width:40px;height:40px;border-radius:50%}
.person b{display:block;font-family:"Poppins",sans-serif;font-weight:700;font-size:16px;line-height:17px;color:var(--ink)}
.person span{font-size:11px;color:var(--olive)}
.dots{left:579px;top:2085px;display:flex;gap:6px}
.dots i{width:6px;height:6px;border-radius:50%;border:1px solid #888}
.dots i.on{background:#444;border-color:#444}
/* details */
.detail{width:200px;text-align:center}
.detail svg{display:block;margin:0 auto}
.detail h4{font-family:"Poppins",sans-serif;font-weight:600;font-size:19px;margin-top:50px;color:var(--ink-soft)}
.detail p{font-size:14px;margin-top:14px;color:var(--ink-soft)}
/* on demand */
.demand-bg{left:0;top:2700px;width:1200px;height:625px}
.demand{left:609px;top:2942px;width:420px;color:var(--white)}
.demand .eyebrow{color:var(--white);font-size:16px;font-weight:500}
.demand h2{font-family:"Poppins",sans-serif;font-weight:700;font-size:39px;margin:12px 0 14px}
.demand p{font-size:16px;line-height:22px}
.btn-light{display:inline-block;margin-top:24px;width:163px;height:48px;line-height:48px;text-align:center;background:var(--white);color:var(--olive-dark);font-weight:500;font-size:17px;letter-spacing:.5px}
/* offer */
.offer{left:0;top:3328px;width:1200px;text-align:center}
.offer .eyebrow{font-size:16px}
.offer h2{font-family:"Poppins",sans-serif;font-weight:700;font-size:48px;line-height:48px;margin-top:20px;color:var(--ink)}
.offer .rule{margin:32px auto 0}
.form{left:424px;top:3582px;width:352px}
.field{border-bottom:1px solid #cfcfcf;font-size:14px;color:#777;padding-bottom:12px;margin-bottom:26px;font-family:Arial,sans-serif}
.field.msg{height:48px;font-family:monospace;font-size:13px}
.send{height:45px;background:var(--olive);color:var(--white);text-align:center;line-height:45px;font-size:14px;font-weight:500;margin-top:-3px}
.footer{left:0;top:3917px;width:1200px;height:72px;background:var(--footer);color:var(--white);text-align:center;line-height:72px;font-size:17px;letter-spacing:.5px}
</style>
</head>
<body>

<!-- hero -->
<svg class="abs hero" viewBox="0 0 1200 830" role="img" aria-label="Photo of a woman doing crunches on a mat in a bright gym">
  <defs>
    <linearGradient id="heroPhoto" x1="0" y1="0" x2="0" y2="1">
      <stop offset="0" stop-color="#f4f2ec"/>
      <stop offset="0.55" stop-color="#d9d2c2"/>
      <stop offset="1" stop-color="#8a5a38"/>
    </linearGradient>
  </defs>
  <rect width="1200" height="830" fill="url(#heroPhoto)"/>
  <path d="M0 770 C300 810 800 700 1200 585 L1200 830 L0 830Z" fill="#8f9a12"/>
  <path d="M0 790 C300 830 560 815 760 770 L760 830 L0 830Z" fill="#2b2b2b"/>
  <path d="M0 828 C450 830 880 760 1200 640 L1200 830 L0 830Z" fill="#ffffff"/>
</svg>
<div class="abs brand"><span>ORBITFIT</span><span class="brand-dot"></span></div>
<nav class="abs nav"><span>HOME</span><span>ABOUT</span><span>SERVICES</span><span>SHOP</span><span>LOGIN</span><span>PRESS</span></nav>
<h1 class="abs hero-title"><span class="l1">TRAIN WITH</span><span class="l2">AWARD-WINNING</span><span class="l3">ORBITFIT P.T.</span></h1>

<!-- intro -->
<section class="abs intro">
  <div class="eyebrow">Personal Training</div>
  <h1>Change Your Body Now!</h1>
  <div class="rule"></div>
  <p>Lorem ipsum dolor sit amet, consectetur adipiscing elit. Cras rutrum in orci sit amet rutrum. Nunc blandit rhoncus consequat. Donec sodales enim et felis commodo, eget posuere turpis fringilla.</p>
</section>

<div class="abs card" style="left:620px;top:874px">
  <div class="ico"><svg width="22" height="22" viewBox="0 0 24 24"><path d="M12 21s-8-5.2-8-11a4.5 4.5 0 0 1 8-2.8A4.5 4.5 0 0 1 20 10c0 5.8-8 11-8 11z" fill="#9aa51c"/></svg></div>
  <h3>Cardio</h3><p>Cras sagittis. Vivamus in erat urna cursus vestibulum.</p>
</div>
<div class="abs card" style="left:848px;top:952px">
  <div class="ico"><svg width="22" height="22" viewBox="0 0 24 24"><path d="M5 19C5 9 11 5 20 5c0 9-5 14-13 13M7 17l7-7" fill="#9aa51c" stroke="#fff" stroke-width="1.4"/></svg></div>
  <h3>Health</h3><p>Cras sagittis. Vivamus in erat urna cursus vestibulum.</p>
</div>
<div class="abs card" style="left:620px;top:1120px">
  <div class="ico"><svg width="22" height="22" viewBox="0 0 24 24"><circle cx="12" cy="12" r="10" fill="#9aa51c"/><path d="M7.5 12.5l3 3 6-6" fill="none" stroke="#fff" stroke-width="2.2"/></svg></div>
  <h3>Fitness</h3><p>Cras sagittis. Vivamus in erat urna cursus vestibulum.</p>
</div>
<div class="abs card" style="left:848px;top:1198px">
  <div class="ico"><svg width="22" height="22" viewBox="0 0 24 24"><path d="M20 4c-6 0-10 4-12 9l3 3c5-2 9-6 9-12zM8 13l-4 1 2-4h3M11 16l-1 4 4-2v-3M5 19l2-2" fill="#9aa51c" stroke="#9aa51c" stroke-width="1"/></svg></div>
  <h3>Agility</h3><p>Cras sagittis. Vivamus in erat urna cursus vestibulum.</p>
</div>

<!-- testimonials -->
<svg class="abs reviews-bg" viewBox="0 0 1200 870" aria-hidden="true">
  <defs>
    <linearGradient id="reviewsGrad" x1="0" y1="1" x2="1" y2="0">
      <stop offset="0" stop-color="#a9b32e"/>
      <stop offset="1" stop-color="#7e8806"/>
    </linearGradient>
  </defs>
  <path d="M0 0 Q600 160 1200 0 L1200 870 Q500 820 0 580Z" fill="url(#reviewsGrad)"/>
</svg>
<h2 class="abs reviews-title">What My<br>Students Say</h2>
<div class="abs rule" style="left:580px;top:1800px;background:#5f6604"></div>

<div class="abs quote" style="left:174px;top:1837px">
  <p>Lorem ipsum dolor sit amet, consectetur adipiscing elit. Nullam porttitor tortor turpis, vel semper massa hendrerit eu.</p>
  <div class="person"><div class="avatar" role="img" aria-label="Student portrait" style="background:linear-gradient(135deg,#c79a78,#5b3a2a)"></div><div><b>Lena P.</b><span>@company</span></div></div>
</div>
<div class="abs quote" style="left:466px;top:1837px">
  <p>Lorem ipsum dolor sit amet, consectetur adipiscing elit. Nullam porttitor tortor turpis, vel semper massa hendrerit eu.</p>
  <div class="person"><div class="avatar" role="img" aria-label="Student portrait" style="background:linear-gradient(135deg,#9a9a9a,#2a2a2a)"></div><div><b>Marco T.</b><span>@company</span></div></div>
</div>
<div class="abs quote" style="left:758px;top:1837px">
  <p>Lorem ipsum dolor sit amet, consectetur adipiscing elit. Nullam porttitor tortor turpis, vel semper massa hendrerit eu.</p>
  <div class="person"><div class="avatar" role="img" aria-label="Student portrait" style="background:linear-gradient(135deg,#d8c09a,#7a8a4a)"></div><div><b>Tessa R.</b><span>@company</span></div></div>
</div>
<div class="abs dots"><i class="on"></i><i></i><i></i><i></i></div>

<!-- session details -->
<div class="abs detail" style="left:157px;top:2402px">
  <svg width="60" height="58" viewBox="0 0 60 58" fill="none" stroke="#9aa51c" stroke-width="2"><rect x="3" y="8" width="54" height="47" rx="4"/><path d="M3 20h54M16 2v12M44 2v12"/></svg>
  <h4>Date</h4><p>Mon-Thu</p>
</div>
<div class="abs detail" style="left:385px;top:2402px">
  <svg width="58" height="58" viewBox="0 0 58 58" fill="none" stroke="#9aa51c" stroke-width="2"><circle cx="29" cy="29" r="26"/><path d="M29 12v17h13"/></svg>
  <h4>Time</h4><p>10 am EST</p>
</div>
<div class="abs detail" style="left:614px;top:2402px">
  <svg width="40" height="58" viewBox="0 0 40 58" fill="none" stroke="#9aa51c" stroke-width="2"><rect x="12" y="2" width="16" height="32" rx="8"/><path d="M5 26c0 9 7 15 15 15s15-6 15-15M20 41v10M11 55h18M12 12h6M12 20h6"/></svg>
  <h4>Duration</h4><p>1 Hour</p>
</div>
<div class="abs detail" style="left:842px;top:2402px">
  <svg width="58" height="58" viewBox="0 0 58 58" fill="none" stroke="#9aa51c" stroke-width="2"><path d="M38 3l17 17-5 5a5 5 0 0 0-7 7l-5 5-3 3L18 57 1 40l17-17 3-3 5-5a5 5 0 0 0 7-7z"/><path d="M25 34c3 3 7 0 5-3s-6-6-3-8 5 0 5 0M22 37l3-3M32 22l3-3"/></svg>
  <h4>Price</h4><p>$50</p>
</div>

<!-- on demand -->
<svg class="abs demand-bg" viewBox="0 0 1200 625" aria-hidden="true">
  <defs>
    <linearGradient id="demandGrad" x1="0" y1="0" x2="1" y2="1">
      <stop offset="0" stop-color="#8f9a10"/>
      <stop offset="1" stop-color="#a7b12c"/>
    </linearGradient>
  </defs>
  <path d="M0 0 Q600 250 1200 0 L1200 625 Q600 470 0 620Z" fill="url(#demandGrad)"/>
</svg>
<div class="abs" role="img" aria-label="Photo of a woman in a sports top lifting a dumbbell" style="left:145px;top:2762px;width:430px;height:500px;border-radius:48% 48% 6px 6px / 30% 30% 6px 6px;background:linear-gradient(180deg,#7a5236 0%,#8a6a55 40%,#5e5e5e 75%,#3a3a3a 100%)"></div>
<section class="abs demand">
  <div class="eyebrow">Any Time. Anywhere</div>
  <h2>On-Demand Classes</h2>
  <p>Access to over 150 online workouts and live-class recordings in varying styles and intensities 24/7.</p>
  <span class="btn-light">SEE PRICING</span>
</section>

<!-- offer -->
<section class="abs offer">
  <div class="eyebrow">Don't Miss Out</div>
  <h2>50% Off<br>For New<br>Students</h2>
  <div class="rule"></div>
</section>
<form class="abs form">
  <div class="field">Full Name</div>
  <div class="field">Email</div>
  <div class="field msg">Message</div>
  <div class="send">Send</div>
</form>

<footer class="abs footer">Copyright 2023 Orbitfit, All rights reserved.</footer>
</body>
</html>
```